Harbourgate Earthmoving – Website Design Brief

Web Design Brief

We are seeking a web designer to build a modern, responsive website for Harbourgate Earthmoving, a Sydney-based earthworks and excavation company.

2. Project Goal
- Build a professional, easy-to-navigate website that:
- Showcases HGE’s capabilities and past projects
- Attracts residential and commercial developers
- Builds credibility and encourages enquiries

3. Target Audience
- Residential developers and home builders
- Commercial construction firms
- Project managers seeking reliable excavation & plant hire services

4. Services to Highlight
- Bulk Excavation
- Detailed Excavation
- Demolition
- Shoring
- Plant Hire

5. Brand Style & Tone
- Clean, bold, and modern
- Professional with a “we get the job done” attitude
- Colors: Lime Green + Concrete Grey (from logo)
- Fonts: Match the modern, rounded, bold typeface in the logo
- Imagery: Showcase big machines, on-site work, before & after shots

6. Website Pages
Recommended structure:
- Home – Quick intro, project highlights, CTA
- About Us – Team story, mission, safety focus
- Services – Separate sections for each core service
- Projects – Case studies or photo gallery
- Plant Hire – Machines available, specs/photos
- Contact – Form + map + details

7. Assets Provided
- Logo (both long + stacked formats)
- Project photos. More can be provided if required.
- Copy: To be drafted

8. Deliverables
Responsive website (desktop/mobile/tablet)
- SEO-ready structure
- CMS (WordPress) for future edits
- Google Maps integration, job enquiry form

Target Market(s)

Target Audience Residential developers and home builders Commercial construction firms Project managers seeking reliable excavation & plant hire services

Industry/Entity Type

Construction

Number of Pages Required

1 page

Requirements
Must have
• Build a professional, easy-to-navigate website that: Showcases HGE’s capabilities and past projects Attracts residential and commercial developers Builds credibility and encourages enquiries
Nice to have
• All provided in the Description
Should not have

```html
<!DOCTYPE html>
<html lang="en">
<head>
<meta charset="utf-8">
<title>Harbourgate Earthmoving – Earthworks Done Right</title>
<link href="https://fonts.googleapis.com/css2?family=Audiowide&family=Poppins:wght@400;500;600;700&display=swap" rel="stylesheet">
<style>
:root{
  --green:#72bf3a;
  --green-dark:#5fa82c;
  --green-light:#a6d77d;
  --ink:#1c1c1c;
  --text:#2f2f2f;
  --grey:#6b6b6b;
  --line:#cfcfcf;
  --white:#ffffff;
  --footer:#1a1a1a;
  --display:"Audiowide",sans-serif;
  --body:"Poppins",sans-serif;
}
*{box-sizing:border-box;margin:0;padding:0}
html,body{width:1200px;height:5111px;overflow:hidden}
body{position:relative;background:var(--white);font-family:var(--body);color:var(--text)}
.abs{position:absolute}
svg{display:block}

/* top bar */
.topbar{left:0;top:0;width:1200px;height:34px;background:var(--ink);color:#ddd;font-size:11px}
.topbar .item{position:absolute;top:0;height:34px;display:flex;align-items:center;gap:7px}
.dot-icon{width:18px;height:18px;border-radius:50%;background:var(--green);display:flex;align-items:center;justify-content:center}

/* header */
.header{left:0;top:34px;width:1200px;height:88px;background:var(--white)}
.logo{position:absolute;font-family:var(--display);color:var(--green);text-transform:uppercase;line-height:1.05}
.header .logo{left:16px;top:22px;font-size:14.5px;letter-spacing:.5px}
.nav{position:absolute;left:0;top:0;height:88px;width:960px}
.nav a{position:absolute;top:36px;font-family:var(--display);font-size:12.5px;color:var(--ink);text-decoration:none;letter-spacing:.5px}
.nav a.active{color:var(--green)}
.nav a.active::after{content:"";position:absolute;left:0;top:-8px;width:14px;height:2px;background:var(--green)}
.agent{position:absolute;left:966px;top:0;width:234px;height:88px;background:var(--green);color:var(--white)}
.agent .ring{position:absolute;left:20px;top:24px;width:40px;height:40px;border-radius:50%;background:var(--white);display:flex;align-items:center;justify-content:center}
.agent small{position:absolute;left:70px;top:24px;font-family:var(--display);font-size:9.5px;letter-spacing:1.5px}
.agent strong{position:absolute;left:70px;top:38px;font-size:20px;font-weight:700}

/* hero */
.hero{left:0;top:122px;width:1200px;height:612px;overflow:hidden}
.hero-photo{position:absolute;inset:0;background:
 radial-gradient(ellipse 45% 40% at 24% 6%,#ffd36b 0,#f2a03d 25%,rgba(216,112,40,.6) 55%,transparent 80%),
 linear-gradient(180deg,#c7702d 0,#8a4520 38%,#4a2b1b 70%,#241712 100%)}
.hero-shade{position:absolute;inset:0;background:linear-gradient(90deg,rgba(0,0,0,.15),rgba(0,0,0,.25) 50%,rgba(0,0,0,.1))}
.hero h1{position:absolute;left:0;width:1200px;top:165px;text-align:center;font-family:var(--display);font-weight:400;font-size:36px;line-height:52px;color:var(--white);letter-spacing:2px}
.hero h1 em{font-style:normal;color:var(--green)}
.hero p{position:absolute;left:0;width:1200px;top:268px;text-align:center;color:var(--white);font-size:21px;font-weight:500;line-height:30px}
.btn{position:absolute;display:flex;align-items:center;justify-content:center;font-family:var(--body);font-weight:600;text-transform:uppercase;font-size:13px;letter-spacing:.5px;text-decoration:none}
.btn-green{background:var(--green);color:var(--white)}
.btn-outline-light{border:2px solid var(--green);color:var(--white);background:rgba(0,0,0,.35)}
.btn-dark{background:var(--ink);color:var(--white)}
.btn-outline{border:2px solid var(--ink);color:var(--ink);background:var(--white)}
.dots{position:absolute;left:562px;top:576px;display:flex;gap:6px}
.dots span{width:13px;height:13px;border-radius:50%;border:1.5px solid #ddd}
.dots span.on{background:var(--green);border-color:var(--green)}

/* about */
.about{left:0;top:734px;width:1200px;height:686px}
.about-photo{position:absolute;left:153px;top:109px;width:476px;height:476px;border-radius:50%;border:14px solid #d7eec4;box-shadow:inset 0 0 0 8px var(--green);background:
 linear-gradient(180deg,#b9c3cc 0,#8d97a0 40%,#7c6d5a 70%,#5d5146 100%)}
.heading{position:absolute;font-family:var(--display);font-weight:400;color:var(--ink);letter-spacing:2px;text-transform:uppercase}
.heading em{font-style:normal;color:var(--green)}
.about .heading{left:691px;top:142px;font-size:27px}
.about .copy{position:absolute;left:691px;top:212px;width:380px;font-size:14.5px;line-height:25px;color:var(--text)}
.divider{position:absolute;height:2px;width:110px;background:var(--green-light)}

/* services */
.services-heading{left:0;width:1200px;top:1518px;text-align:center;font-size:27px}
.card{position:absolute;overflow:hidden}
.card .photo{position:absolute;inset:0}
.card .fade{position:absolute;inset:0;background:linear-gradient(180deg,rgba(0,0,0,0) 30%,rgba(0,0,0,.75) 78%,rgba(0,0,0,.9) 100%)}
.card h3{position:absolute;left:0;width:100%;text-align:center;font-family:var(--display);font-weight:400;color:var(--green);letter-spacing:2px;text-transform:uppercase}
.card p{position:absolute;left:40px;right:40px;text-align:center;color:var(--white);font-size:15.5px;line-height:25px}
.card .mini{position:absolute;left:50%;transform:translateX(-50%);width:84px;height:24px;background:var(--green);color:var(--white);font-size:8.5px;font-weight:600;display:flex;align-items:center;justify-content:center;text-transform:uppercase;border-radius:2px}
.ph-earth{background:linear-gradient(180deg,#9aa3a6 0,#7b7d74 35%,#6a5a47 60%,#3d3428 100%)}
.ph-rock{background:linear-gradient(180deg,#8ea4b8 0,#a99474 40%,#7d6246 70%,#3a2d22 100%)}
.ph-dust{background:linear-gradient(180deg,#6d7f8c 0,#a2a29a 35%,#8a8a6e 60%,#2f2f2a 100%)}
.ph-night{background:linear-gradient(180deg,#1c3a55 0,#2e4b62 40%,#3a3f3f 70%,#151515 100%)}
.ph-yellow{background:linear-gradient(180deg,#8da0ae 0,#a59a72 35%,#b79a2f 55%,#3b3320 100%)}

/* projects */
.projects-band{left:0;top:2702px;width:1200px;height:516px;background:var(--green)}
.projects .heading{right:706px;top:2803px;font-size:27px}
.projects .copy{position:absolute;left:66px;width:428px;top:2884px;text-align:right;font-size:14.5px;line-height:25px;color:var(--ink)}
.tile{position:absolute;width:304px;height:288px;overflow:hidden;background:var(--white)}
.tile .photo{position:absolute;left:0;top:0;right:0;bottom:0}
.tile h3{position:absolute;left:0;width:100%;bottom:26px;text-align:center;font-family:var(--display);font-weight:400;font-size:20px;line-height:34px;color:var(--green);letter-spacing:2px}
.ph-aerial{background:linear-gradient(180deg,#c9c9c5 0,#8f8e88 40%,#5d5b55 70%,#1e1e1e 100%)}
.ph-basement{background:linear-gradient(180deg,#b6c4cc 0,#9a8a6a 45%,#6b553b 70%,#1e1a15 100%)}
.ph-demo{background:linear-gradient(180deg,#c9d4dc 0,#9b8f7e 45%,#6e4d37 70%,#1c1713 100%)}
.ph-split{background:linear-gradient(90deg,#8a6d5b 0,#7a5e4d 50%,#dfe3e6 52%,#b8c1c6 100%)}
.tile .shade{position:absolute;inset:0;background:linear-gradient(180deg,rgba(0,0,0,0) 40%,rgba(0,0,0,.8) 100%)}

/* plant hire */
.plant-heading{left:0;width:1200px;top:3390px;text-align:center;font-size:27px}
.plant-intro{left:270px;width:660px;top:3468px;text-align:center;font-size:15.5px;line-height:28px;color:var(--ink)}
.machine{position:absolute;top:3543px;width:270px}
.machine .photo{height:203px;width:100%;background:linear-gradient(90deg,#7e7d78 0,#9a8f7d 48%,#c7d1d8 52%,#8ea4b6 100%)}
.machine.featured .photo{outline:5px solid var(--green);outline-offset:-5px}
.machine span{display:block;margin-top:22px;text-align:center;font-weight:600;font-size:16.5px;color:var(--ink)}
.plant-note{left:0;width:1200px;top:3815px;text-align:center;font-size:16px;color:var(--ink)}

/* contact */
.skyline{left:0;top:4380px;width:1200px;height:322px;background:linear-gradient(180deg,rgba(255,255,255,1) 0,rgba(226,233,238,.9) 30%,#9fb1bd 62%,#5e6d74 85%,#3f4a4c 100%)}
.map{left:75px;top:4032px;width:486px;height:508px;border:8px solid var(--green);background:
 linear-gradient(135deg,#eef1ec 0,#e2eadf 40%,#dfe8e4 70%,#eceee9 100%)}
.contact .heading{left:601px;top:4032px;font-size:27px}
.contact .copy{position:absolute;left:602px;top:4096px;width:440px;font-size:14px;line-height:24px;color:var(--text)}
.field{position:absolute;left:605px;width:562px;height:40px;border:1.5px solid var(--line);background:var(--white);display:flex;align-items:center;gap:12px;padding-left:14px;font-size:13.5px;color:var(--text)}
.field.message{height:137px;align-items:flex-start;padding-top:12px}

/* footer */
.footer{left:0;top:4702px;width:1200px;height:409px;background:var(--footer);color:#e9e9e9}
.footer .logo{left:131px;top:78px;font-size:22px;letter-spacing:1px}
.social{position:absolute;top:222px;width:36px;height:36px;border-radius:50%;border:2px solid var(--green)}
.social.on{background:var(--green)}
.foot-col{position:absolute;top:76px}
.foot-col h4{font-family:var(--display);font-weight:400;font-size:15px;letter-spacing:2px;color:var(--white);text-transform:uppercase}
.foot-col h4::after{content:"";display:block;width:34px;height:2px;background:var(--green);margin-top:6px}
.foot-col ul{list-style:none;margin-top:20px}
.foot-col li{font-size:12px;line-height:26px;color:#ddd}
.contact-row{position:absolute;left:796px;display:flex;align-items:center;gap:14px}
.contact-row .ic{width:30px;height:30px;border-radius:50%;border:1px solid #555;display:flex;align-items:center;justify-content:center}
.contact-row small{display:block;font-size:9px;color:#bbb}
.contact-row b{display:block;font-size:12px;font-weight:600;color:var(--white)}
.foot-rule{left:111px;top:296px;width:980px;height:1px;background:var(--green)}
.totop{left:1128px;top:278px;width:40px;height:40px;border-radius:4px;background:var(--green);display:flex;align-items:center;justify-content:center}
.copyright{left:0;width:1200px;top:350px;text-align:center;font-size:13px;color:#ccc}
</style>
</head>
<body>

<!-- top bar -->
<div class="abs topbar">
  <div class="item" style="left:122px">
    <span class="dot-icon"><svg width="10" height="12" viewBox="0 0 10 12"><path d="M5 0a4 4 0 0 1 4 4c0 3-4 8-4 8S1 7 1 4a4 4 0 0 1 4-4z" fill="#fff"/><circle cx="5" cy="4" r="1.5" fill="#72bf3a"/></svg></span>
    18 Wharf Lane, Marrickville NSW 2204
  </div>
  <div class="item" style="left:922px">
    <span class="dot-icon"><svg width="11" height="8" viewBox="0 0 11 8"><rect x=".5" y=".5" width="10" height="7" fill="none" stroke="#fff"/><path d="M.5.5l5 4 5-4" fill="none" stroke="#fff"/></svg></span>
    info@harbourgateearth.com.au
  </div>
</div>

<!-- header -->
<header class="abs header">
  <div class="logo">Harbourgate<br>Earthmoving</div>
  <nav class="nav">
    <a class="active" style="left:163px">HOME</a>
    <a style="left:258px">ABOUT US</a>
    <a style="left:395px">SERVICES</a>
    <a style="left:528px">PROJECTS</a>
    <a style="left:670px">PLANT HIRE</a>
    <a style="left:825px">CONTACT US</a>
  </nav>
  <div class="agent">
    <span class="ring"><svg width="18" height="18" viewBox="0 0 24 24"><path d="M6.6 10.8a15 15 0 0 0 6.6 6.6l2.2-2.2a1 1 0 0 1 1-.25 11.4 11.4 0 0 0 3.6.57 1 1 0 0 1 1 1V20a1 1 0 0 1-1 1A17 17 0 0 1 3 4a1 1 0 0 1 1-1h3.5a1 1 0 0 1 1 1c0 1.25.2 2.45.57 3.57a1 1 0 0 1-.25 1z" fill="#1c1c1c"/></svg></span>
    <small>TALK TO AN AGENT</small>
    <strong>02 5550 1824</strong>
  </div>
</header>

<!-- hero -->
<section class="abs hero">
  <div class="hero-photo" role="img" aria-label="Sunset over an earthworks site with a bulldozer and a worker in hard hat and hi-vis vest"></div>
  <div class="hero-shade"></div>
  <h1>EARTHWORKS DONE <em>RIGHT.</em><br>ON <em>TIME.</em> EVERY <em>TIME.</em></h1>
  <p>Bulk &amp; Detailed Excavation, Demolition, Shoring<br>&amp; Plant Hire – Sydney-Wide.</p>
  <a class="btn btn-green" style="left:423px;top:356px;width:140px;height:44px">Get a Quote</a>
  <a class="btn btn-outline-light" style="left:578px;top:356px;width:142px;height:44px">View Our Work</a>
  <div class="dots"><span></span><span class="on"></span><span></span><span></span></div>
</section>

<!-- about -->
<section class="abs about">
  <svg class="abs" style="left:0;top:0" width="540" height="686" viewBox="0 0 540 686">
    <polygon points="0,0 540,0 282,686 0,686" fill="#7cc242"/>
    <polygon points="0,0 300,0 0,430" fill="#8ccb57"/>
  </svg>
  <div class="about-photo" role="img" aria-label="Site engineer with tablet standing beside a road roller"></div>
  <h2 class="heading"><em>About</em> Us</h2>
  <p class="copy">Built on Experience. Driven by Results.<br>Harbourgate Earthmoving is a family-run business serving Sydney's construction industry with dependable excavation and earthmoving solutions. With decades of combined experience, our crew prides itself on site safety, operational efficiency, and genuine client relationships.</p>
  <a class="btn btn-green" style="left:691px;top:411px;width:142px;height:44px">Learn More</a>
</section>

<!-- services -->
<h2 class="abs heading services-heading"><em>Our</em> Services</h2>
<div class="abs divider" style="left:545px;top:1574px"></div>

<article class="card" style="left:111px;top:1605px;width:976px;height:290px">
  <div class="photo ph-earth" role="img" aria-label="Excavators clearing a large earthworks site"></div>
  <div class="fade"></div>
  <h3 style="top:160px;font-size:27px">Bulk Excavation</h3>
  <p style="top:206px">We remove large volumes of soil and rock to prepare your site for construction. Our skilled operators and fleet of powerful machinery make quick work of complex digs.</p>
</article>

<article class="card" style="left:111px;top:1926px;width:304px;height:290px">
  <div class="photo ph-rock" role="img" aria-label="Excavator arm cutting into a rock face"></div>
  <div class="fade"></div>
  <h3 style="top:188px;font-size:19px;line-height:26px">Detailed<br>Excavation</h3>
  <span class="mini" style="top:246px">Learn More</span>
</article>
<article class="card" style="left:448px;top:1926px;width:304px;height:290px">
  <div class="photo ph-dust" role="img" aria-label="Yellow excavator demolishing a building in a cloud of dust"></div>
  <div class="fade"></div>
  <h3 style="top:208px;font-size:19px">Demolition</h3>
  <span class="mini" style="top:246px">Learn More</span>
</article>
<article class="card" style="left:784px;top:1926px;width:304px;height:290px">
  <div class="photo ph-night" role="img" aria-label="Workers inspecting shoring walls at night"></div>
  <div class="fade"></div>
  <h3 style="top:208px;font-size:19px">Shoring</h3>
  <span class="mini" style="top:246px">Learn More</span>
</article>

<article class="card" style="left:111px;top:2248px;width:976px;height:288px">
  <div class="photo ph-yellow" role="img" aria-label="Line-up of yellow earthmoving machines"></div>
  <div class="fade"></div>
  <h3 style="top:160px;font-size:27px">Plant Hire</h3>
  <p style="top:206px">Need equipment? We offer wet and dry hire of excavators, posi tracks, tipper trucks and more. All machines are regularly serviced and come with experienced operators.</p>
</article>

<!-- projects -->
<section class="projects">
  <div class="abs projects-band"></div>
  <h2 class="abs heading" style="right:706px;top:2803px;font-size:27px">Our Projects</h2>
  <p class="copy">Kaerspiciatis unde omnis iste natus error sit voluptatem accusantium doloremque laudantium, totam rem aperiam, eaque ipsa quae ab illo inventore veritatis et quasi architecto beatae vitae dicta sunt explicabo. Nemo enim ipsam voluptatem quia voluptas sit aspernatur aut odit aut fugit, sed quia consequuntur magni dolorem.</p>
  <a class="btn btn-dark" style="left:115px;top:3081px;width:185px;height:44px">View All Projects</a>
  <a class="btn btn-outline" style="left:313px;top:3081px;width:180px;height:44px">Enquire Now</a>

  <article class="tile" style="left:524px;top:2649px">
    <div class="photo ph-aerial" role="img" aria-label="Aerial view of multi-unit residential site"></div><div class="shade"></div>
    <h3>MULTI-UNIT<br>RESIDENTIAL<br>SITE PREPS</h3>
  </article>
  <article class="tile" style="left:855px;top:2649px">
    <div class="photo ph-basement" role="img" aria-label="Excavator digging a basement"></div><div class="shade"></div>
    <h3>BASEMENT<br>EXCAVATIONS</h3>
  </article>
  <article class="tile" style="left:524px;top:2972px">
    <div class="photo ph-demo" role="img" aria-label="Excavator demolishing a commercial building"></div><div class="shade"></div>
    <h3>COMMERCIAL<br>DEMOLITION JOBS</h3>
  </article>
  <article class="tile" style="left:855px;top:2972px">
    <div class="photo ph-split" role="img" aria-label="Before and after view of a building site"></div><div class="shade"></div>
    <h3>BEFORE/AFTER<br>COMPARISONS</h3>
  </article>
</section>

<!-- plant hire -->
<h2 class="abs heading plant-heading"><em>Plant</em> Hire</h2>
<div class="abs divider" style="left:545px;top:3445px"></div>
<p class="abs plant-intro">Machines You Can Rely On. From compact digs to major clear-outs, we offer a fleet of quality machines including:</p>
<div class="machine" style="left:36px"><div class="photo" role="img" aria-label="Before and after of a cleared site and new tower"></div><span>KCASOIEC CASELICS</span></div>
<div class="machine featured" style="left:325px"><div class="photo" role="img" aria-label="Before and after of a demolished block and new building"></div><span>KCASOIEC CASELICS</span></div>
<div class="machine" style="left:615px"><div class="photo" role="img" aria-label="Before and after of a city site and glass tower"></div><span>KCASOIEC CASELICS</span></div>
<div class="machine" style="left:903px"><div class="photo" role="img" aria-label="Before and after of rubble and finished skyscraper"></div><span>KCASOIEC CASELICS</span></div>
<p class="abs plant-note">All plant is available for short- or long-term hire. Flexible packages available.</p>
<a class="btn btn-green" style="left:403px;top:3861px;width:180px;height:44px">Check Availability</a>
<a class="btn btn-outline" style="left:598px;top:3861px;width:200px;height:44px">Download Spec Sheet</a>

<!-- contact -->
<section class="contact">
  <div class="abs skyline" role="img" aria-label="Excavators in front of a city skyline"></div>
  <div class="abs map" role="img" aria-label="Street map showing the office location"></div>
  <h2 class="abs heading"><em>Contact</em> Us</h2>
  <p class="copy">Let's Talk Dirt. Looking to start your next project? Reach out below or call us directly.</p>
  <div class="field" style="top:4158px"><svg width="16" height="16" viewBox="0 0 16 16"><circle cx="8" cy="5" r="3.5" fill="#72bf3a"/><path d="M1 16c0-4 3-6 7-6s7 2 7 6z" fill="#72bf3a"/></svg>Your Name</div>
  <div class="field" style="top:4218px"><svg width="16" height="12" viewBox="0 0 16 12"><rect width="16" height="12" rx="1" fill="#72bf3a"/><path d="M1 1l7 5 7-5" fill="none" stroke="#fff" stroke-width="1.3"/></svg>Email</div>
  <div class="field" style="top:4278px"><svg width="15" height="15" viewBox="0 0 24 24"><path d="M6.6 10.8a15 15 0 0 0 6.6 6.6l2.2-2.2a1 1 0 0 1 1-.25 11.4 11.4 0 0 0 3.6.57 1 1 0 0 1 1 1V20a1 1 0 0 1-1 1A17 17 0 0 1 3 4a1 1 0 0 1 1-1h3.5a1 1 0 0 1 1 1c0 1.25.2 2.45.57 3.57a1 1 0 0 1-.25 1z" fill="#72bf3a"/></svg>Phone Number</div>
  <div class="field message" style="top:4337px"><svg width="18" height="16" viewBox="0 0 18 16"><rect x="0" y="0" width="12" height="9" rx="1.5" fill="#72bf3a"/><rect x="5" y="5" width="13" height="8" rx="1.5" fill="#8ccb57"/><path d="M14 13v3l-3-3z" fill="#8ccb57"/></svg>Write A Message</div>
  <a class="btn btn-green" style="left:605px;top:4498px;width:175px;height:44px">Send Message</a>
</section>

<!-- footer -->
<footer class="abs footer">
  <div class="logo">Harbourgate<br>Earthmoving</div>
  <span class="social" style="left:125px" role="img" aria-label="Social profile one"></span>
  <span class="social on" style="left:176px" role="img" aria-label="Social profile two"></span>
  <span class="social" style="left:232px" role="img" aria-label="Social profile three"></span>

  <div class="foot-col" style="left:411px"><h4>Quick Links</h4>
    <ul><li>Home</li><li>About Us</li><li>Services</li><li>Projects</li><li>Plant Hire</li><li>Contact Us</li></ul></div>
  <div class="foot-col" style="left:629px"><h4>Links</h4>
    <ul><li>Copyright</li><li>Legal</li><li>Privacy</li><li>Accessibility</li><li>Sitemap</li></ul></div>
  <div class="foot-col" style="left:796px"><h4>Contact Us</h4></div>

  <div class="contact-row" style="top:138px"><span class="ic"><svg width="13" height="13" viewBox="0 0 24 24"><path d="M6.6 10.8a15 15 0 0 0 6.6 6.6l2.2-2.2a1 1 0 0 1 1-.25 11.4 11.4 0 0 0 3.6.57 1 1 0 0 1 1 1V20a1 1 0 0 1-1 1A17 17 0 0 1 3 4a1 1 0 0 1 1-1h3.5a1 1 0 0 1 1 1c0 1.25.2 2.45.57 3.57a1 1 0 0 1-.25 1z" fill="#fff"/></svg></span><div><small>Call Us</small><b>02 5550 1824</b></div></div>
  <div class="contact-row" style="top:188px"><span class="ic"><svg width="13" height="10" viewBox="0 0 16 12"><rect width="16" height="12" rx="1" fill="#fff"/><path d="M1 1l7 5 7-5" fill="none" stroke="#1a1a1a" stroke-width="1.3"/></svg></span><div><small>Email</small><b>info@harbourgateearth.com.au</b></div></div>
  <div class="contact-row" style="top:238px"><span class="ic"><svg width="11" height="14" viewBox="0 0 10 12"><path d="M5 0a4 4 0 0 1 4 4c0 3-4 8-4 8S1 7 1 4a4 4 0 0 1 4-4z" fill="#fff"/><circle cx="5" cy="4" r="1.5" fill="#1a1a1a"/></svg></span><div><small>Address</small><b>18 Wharf Lane, Marrickville NSW 2204</b></div></div>

  <div class="abs foot-rule"></div>
  <div class="abs totop"><svg width="16" height="10" viewBox="0 0 16 10"><path d="M2 8l6-6 6 6" fill="none" stroke="#fff" stroke-width="2.5"/></svg></div>
  <p class="abs copyright">© 2025 .All rights reserved.</p>
</footer>

</body>
</html>
```